KB Rubbish Removal Business Card

Hey,
I need a double sided business card designed for a rubbish removal business based in Australia. Logo is already chosen, similar colours preferred for both sides of the business card.

Details to include:

Front:

KB Rubbish Removal
Darren Holloway
Managing Director
Mobile: 0471 902 146
Email: darren@kbrubbishremoval.com.au
Website: kbrubbishremoval.com.au

Rear:

How did we do?
kbrubbishremoval.com.au/review

```html
<!DOCTYPE html>
<html lang="en">
<head>
<meta charset="utf-8">
<title>KB Rubbish Removal – Business Card</title>
<link href="https://fonts.googleapis.com/css2?family=Khand:wght@600&family=Roboto:wght@400;500&display=swap" rel="stylesheet">
<style>
  :root {
    --backdrop: #1e1e1e;
    --green-deep: #0b7a1f;
    --green-mid: #12a031;
    --green-bright: #18ab36;
    --green-lime: #8fd44a;
    --paper: #eeeeec;
    --paper-shade: #dcdcda;
    --ink-light: #f2f4f0;
  }
  * { margin: 0; padding: 0; box-sizing: border-box; }
  html, body { width: 1200px; height: 1138px; overflow: hidden; background: var(--backdrop); }
  .canvas { position: relative; width: 1200px; height: 1138px; }

  .card {
    position: absolute;
    border-radius: 14px;
    overflow: hidden;
  }

  /* Review side */
  .card-review {
    left: 274px; top: 185px; width: 623px; height: 377px;
    background: radial-gradient(circle at 78% 55%, #056a14 0%, var(--green-deep) 30%, transparent 60%),
                linear-gradient(135deg, var(--green-bright) 0%, var(--green-mid) 45%, var(--green-deep) 100%);
  }
  .review-heading {
    position: absolute; left: 36px; top: 30px;
    font-family: "Khand", sans-serif; font-weight: 600;
    font-size: 54px; line-height: 50px; letter-spacing: 0.5px;
    color: var(--ink-light);
  }
  .review-link {
    position: absolute; left: 36px; top: 313px;
    font-family: "Roboto", sans-serif; font-weight: 500;
    font-size: 19px; color: var(--ink-light);
  }

  /* Contact side */
  .card-contact {
    left: 276px; top: 608px; width: 618px; height: 374px;
    background: linear-gradient(160deg, var(--green-bright) 0%, var(--green-mid) 55%, #0e8f2a 100%);
  }
  .contact-panel { position: absolute; inset: 0; }
  .brand-block {
    position: absolute; left: 30px; top: 156px; width: 190px;
    display: flex; align-items: center; gap: 10px;
    font-family: "Khand", sans-serif; font-weight: 600;
    font-size: 24px; line-height: 24px; color: var(--green-mid);
  }
  .brand-dot { width: 22px; height: 22px; border-radius: 50%; background: var(--green-mid); flex: none; }

  .company-name {
    position: absolute; left: 306px; top: 84px;
    font-family: "Khand", sans-serif; font-weight: 600;
    font-size: 32px; letter-spacing: 1px; word-spacing: 4px;
    color: var(--ink-light);
  }
  .person-name {
    position: absolute; left: 306px; top: 150px;
    font-family: "Roboto", sans-serif; font-weight: 500;
    font-size: 22px; color: var(--ink-light);
  }
  .person-role {
    position: absolute; left: 306px; top: 178px;
    font-family: "Roboto", sans-serif; font-weight: 400;
    font-size: 15px; color: var(--ink-light);
  }
  .divider {
    position: absolute; left: 306px; top: 205px; width: 222px; height: 1.5px;
    background: var(--ink-light);
  }
  .contact-list { position: absolute; left: 306px; top: 216px; list-style: none; }
  .contact-item {
    display: flex; align-items: center; height: 24px;
    font-family: "Roboto", sans-serif; font-size: 16px; color: var(--ink-light);
  }
  .contact-icon { width: 14px; height: 14px; margin-right: 16px; flex: none; }
</style>
</head>
<body>
<div class="canvas">

  <section class="card card-review" aria-label="Review side">
    <h2 class="review-heading">HOW DID<br>WE DO?</h2>
    <p class="review-link">kbrubbishremoval.com.au/review</p>
  </section>

  <section class="card card-contact" aria-label="Contact side">
    <svg class="contact-panel" width="618" height="374" viewBox="0 0 618 374" aria-hidden="true">
      <defs>
        <linearGradient id="paperFill" x1="0" y1="0" x2="0" y2="1">
          <stop offset="0" stop-color="#f1f1ef"/>
          <stop offset="1" stop-color="#dadad8"/>
        </linearGradient>
        <linearGradient id="edgeGlow" x1="0" y1="0" x2="0" y2="1">
          <stop offset="0" stop-color="#1aa838"/>
          <stop offset="0.6" stop-color="#8fd44a"/>
          <stop offset="1" stop-color="#2fb53f"/>
        </linearGradient>
      </defs>
      <path d="M0 0 H218 Q340 187 218 374 H0 Z" fill="url(#edgeGlow)"/>
      <path d="M0 0 H205 Q322 187 205 374 H0 Z" fill="url(#paperFill)"/>
    </svg>

    <div class="brand-block">
      <span class="brand-dot"></span>
      <span>KB Rubbish Removal</span>
    </div>

    <h1 class="company-name">KB RUBBISH REMOVAL</h1>
    <p class="person-name">Darren Holloway</p>
    <p class="person-role">Managing Director</p>
    <div class="divider"></div>

    <ul class="contact-list">
      <li class="contact-item">
        <svg class="contact-icon" viewBox="0 0 14 14" aria-hidden="true"><path d="M1 5 Q7 0 13 5 L11 6.5 L9.5 5 H4.5 L3 6.5 Z M3 7 H11 L12 12 H2 Z" fill="#f2f4f0"/></svg>
        0471 902 146
      </li>
      <li class="contact-item">
        <svg class="contact-icon" viewBox="0 0 14 14" aria-hidden="true"><rect x="1" y="3" width="12" height="8" fill="#f2f4f0"/><path d="M1 3 L7 8 L13 3 M1 11 L5.5 7 M13 11 L8.5 7" stroke="#12a031" stroke-width="1.2" fill="none"/></svg>
        darren@kbrubbishremoval.com.au
      </li>
      <li class="contact-item">
        <svg class="contact-icon" viewBox="0 0 14 14" aria-hidden="true"><circle cx="7" cy="7" r="5.5" fill="none" stroke="#f2f4f0" stroke-width="1.3"/><ellipse cx="7" cy="7" rx="2.3" ry="5.5" fill="none" stroke="#f2f4f0" stroke-width="1.1"/><path d="M1.5 7 H12.5" stroke="#f2f4f0" stroke-width="1.1"/></svg>
        www.kbrubbishremoval.com.au
      </li>
    </ul>
  </section>

</div>
</body>
</html>
```